Poster Design Project

About Us
Lumvik is a company that specializes in providing communication solutions to the travel market. Our simple vision of “every hotel should have a mobile phone in the guest rooms”, led us to develop a path breaking cost effective mobile phone. With full integration capabilities with the hotels property management system, location based marketing, user locator and other features, this product is unique in addressing the hospitality segment.
Product Placement
The Lumvik mobile will be placed in the hotel room on an A4 Sized transparent stand (the transparent stand is attached for your reference. If you notice, the phone will be placed in the jacket on the bottom left and in another jacket on the bottom right will be the brochure. So effectively, the design space available on the A4 brochure is only 60% of the space). The designed poster that we wish designed will be inserted in the A4 sized acrylic stand. The stand would typically be on the bedside table or on the study table of the hotel room. The A4 design should be bright and vibrant in keeping with our logo colors.
Attached is our logo. Also attached is the symbol of our phone that could be used innovatively on the brochure if you think it helps.
Attached is the content for the poster.
Reason: Feedback from the management team got delayed, hence the extension. Thanks
Reason: The delay is in the content finalization.

```html
<!DOCTYPE html>
<html lang="en">
<head>
<meta charset="utf-8">
<title>Lumvik — Keep Talking</title>
<link rel="stylesheet" href="https://fonts.googleapis.com/css2?family=Arimo:ital,wght@0,400;0,700;1,400&family=Michroma&display=swap">
<style>
  :root {
    --orange-deep: #f07f12;
    --orange-mid: #f9a54a;
    --orange-light: #fde0b8;
    --ink: #111111;
    --white: #ffffff;
    --grey-dot: #b9b9b9;
    --grey-light: #eeeeee;
  }
  html, body { margin: 0; padding: 0; overflow: hidden; }
  body { width: 849px; height: 1200px; background: var(--white); }
  .poster {
    position: relative;
    width: 849px;
    height: 1200px;
    overflow: hidden;
    background: var(--white);
    font-family: "Arimo", Arial, sans-serif;
    color: var(--ink);
  }
  .backdrop { position: absolute; inset: 0; }
  .brand {
    position: absolute;
    top: 18px; left: 0; right: 0;
    display: flex; justify-content: center; align-items: center; gap: 14px;
  }
  .brand-mark {
    width: 22px; height: 22px; border-radius: 50%;
    background: var(--orange-deep);
  }
  .brand-name {
    font-family: "Michroma", "Arimo", sans-serif;
    font-size: 74px; font-weight: 400;
    letter-spacing: 4px;
    color: var(--ink);
    line-height: 1;
  }
  .headline {
    position: absolute; top: 124px; left: 0; right: 0;
    margin: 0; text-align: center;
    font-size: 33px; font-weight: 700;
  }
  .offer {
    position: absolute; top: 198px; left: 0; right: 0;
    margin: 0; padding: 0; list-style: none;
    text-align: center;
    font-size: 28px; line-height: 31.5px; font-weight: 400;
  }
  .offer strong { font-weight: 700; }
  .offer .plus { font-size: 26px; }
  .tagline {
    position: absolute; top: 520px; left: 0; right: 0;
    margin: 0; text-align: center;
    font-size: 31px; font-weight: 700;
    text-decoration: underline; text-underline-offset: 5px;
  }
  .blurbs {
    position: absolute; top: 566px; left: 0; right: 0;
    margin: 0; text-align: center;
    font-size: 21px; line-height: 28px;
  }
  .blurbs .note { font-weight: 700; text-decoration: underline; }
  .footnote {
    position: absolute; left: 24px; bottom: 22px;
    margin: 0; font-size: 19px; font-style: italic;
  }
  .halftone {
    position: absolute; left: 0; right: 0; top: 700px; height: 500px;
  }
  .badge { position: absolute; left: 560px; top: 830px; }
</style>
</head>
<body>
<main class="poster">
  <svg class="backdrop" width="849" height="1200" viewBox="0 0 849 1200" aria-hidden="true">
    <defs>
      <linearGradient id="orangeField" x1="0" y1="0" x2="0" y2="1">
        <stop offset="0" stop-color="var(--orange-light)"/>
        <stop offset="0.35" stop-color="var(--orange-mid)"/>
        <stop offset="1" stop-color="var(--orange-deep)"/>
      </linearGradient>
      <linearGradient id="greyFade" x1="0" y1="0" x2="0" y2="1">
        <stop offset="0" stop-color="var(--white)"/>
        <stop offset="1" stop-color="var(--grey-light)"/>
      </linearGradient>
    </defs>
    <path d="M0 190 C 200 175, 600 175, 849 195 L 849 760 C 620 700, 300 640, 0 700 Z" fill="url(#orangeField)"/>
    <path d="M0 640 C 250 600, 520 640, 849 600 L 849 1200 L 0 1200 Z" fill="url(#greyFade)"/>
    <path d="M0 700 C 280 640, 560 700, 849 760 L 849 800 C 560 740, 270 690, 0 740 Z" fill="var(--orange-deep)" opacity="0.9"/>
    <path d="M0 665 C 260 620, 560 670, 849 720" stroke="var(--white)" stroke-width="5" fill="none" opacity="0.8"/>
    <path d="M0 755 C 260 715, 540 760, 849 820" stroke="var(--orange-mid)" stroke-width="4" fill="none"/>
  </svg>

  <div class="halftone" role="img" aria-label="Grey halftone dot texture fading across the lower area" style="background: radial-gradient(ellipse at 20% 30%, rgba(185,185,185,0.55), rgba(238,238,238,0) 70%);"></div>

  <header class="brand">
    <span class="brand-name">LUMVIK</span>
    <span class="brand-mark"></span>
  </header>

  <h1 class="headline">Pick up this phone NOW, to keep talking...</h1>

  <ul class="offer">
    <li><strong>SAVE 80%</strong> on international roaming</li>
    <li class="plus">+</li>
    <li>Get a <strong>LOCAL</strong> number</li>
    <li class="plus">+</li>
    <li><strong>60 FREE</strong> minutes of international Calls</li>
    <li class="plus">+</li>
    <li><strong>60 FREE</strong> minutes of local calls</li>
    <li class="plus">+</li>
    <li>= 499 BHT</li>
  </ul>

  <p class="tagline">Lumvik. Keep Talking.</p>

  <p class="blurbs">
    <span class="note">The following needs to appear as blurbs</span> - Itemized bill on checkout<br>
    Flexible tariff plans to choose from<br>
    Excellent call quality
  </p>

  <svg class="badge" width="270" height="270" viewBox="0 0 270 270" aria-hidden="true">
    <circle cx="135" cy="135" r="132" fill="var(--ink)"/>
    <circle cx="135" cy="135" r="118" fill="var(--orange-deep)"/>
    <circle cx="135" cy="135" r="96" fill="var(--ink)"/>
  </svg>

  <p class="footnote">Refer to the brochure for more details</p>
</main>
</body>
</html>
```